Commercial, Public Works, Contractor needs a modern web design

We are a General and Engineering contracting firm with vast experience in our industry. Our focus is on Commercial, Tenant Improvement, Restaurants, and Public Works. We are opening a new business and would like that excitement and energy to show through the new web design. The colors we like are black, red and grey, we are open to color ideas. Attached is our logo design.

Industry/Entity Type

Restaurant

```html
<!DOCTYPE html>
<html lang="en">
<head>
<meta charset="utf-8">
<title>Ridgeline Builders, Inc.</title>
<link href="https://fonts.googleapis.com/css2?family=Raleway:wght@400;500;600&family=Open+Sans:wght@400;600;700&family=Arimo:wght@400&display=swap" rel="stylesheet">
<style>
:root{
  --red:#c0141b;
  --red-dark:#a50f15;
  --red-band:#b30f16;
  --red-active:#c8161d;
  --ink:#333;
  --muted:#777;
  --footer:#2b2e34;
  --footer-deep:#202227;
  --white:#fff;
}
*{box-sizing:border-box;margin:0;padding:0}
html,body{width:741px;height:1200px;overflow:hidden;background:var(--white)}
body{position:relative;font-family:"Arimo",Arial,sans-serif;color:var(--ink)}
.abs{position:absolute}
.top-rule{left:0;top:0;width:741px;height:2px;background:var(--red)}
.brand{left:60px;top:31px;font:700 11px "Open Sans",sans-serif;color:var(--red);display:flex;align-items:center;gap:5px;letter-spacing:.2px}
.brand .mark{width:10px;height:10px;border-radius:50%;background:var(--red)}
.nav{left:302px;top:34px;display:flex;gap:22px;font:400 8px "Open Sans",sans-serif;color:#555}
.nav span::before{content:"";display:inline-block;width:4px;height:4px;border:1px solid #999;border-radius:50%;margin-right:4px;vertical-align:1px}
.nav .active{color:var(--red)}
.nav .active::before{border-color:var(--red)}
.hero{left:0;top:74px;width:741px;height:320px;background:linear-gradient(135deg,#4a4c50,#6d7075 55%,#555759)}
.hero-caption{left:0;top:358px;width:741px;height:36px;background:rgba(30,30,32,.45);display:flex;align-items:center;justify-content:center;gap:14px}
.hero-caption h1{font:400 16.5px "Raleway",sans-serif;color:var(--white);letter-spacing:-.3px}
.arrow{width:18px;height:18px;border-radius:50%;background:var(--white);display:flex;align-items:center;justify-content:center}
.service{width:290px;height:100px}
.service .thumb{left:0;top:0;width:72px;height:62px;border:2px solid #eee}
.service h2{left:85px;top:2px;font:400 12px "Raleway",sans-serif;color:#333}
.service p{left:85px;top:22px;width:212px;font-size:6px;line-height:11.6px;color:var(--muted)}
.service .more{left:85px;top:72px;font-size:8px;color:var(--red)}
.band{left:0;top:654px;width:741px;height:209px;background:var(--red-band)}
.tabs{left:61px;top:654px;width:619px;height:31px;background:var(--red-dark)}
.tabs .lead{left:0;top:0;width:67px;height:31px;background:#9c0d13}
.tabs svg{position:absolute;left:0;top:0}
.tab-label{top:11px;font:600 7px "Open Sans",sans-serif;color:var(--white);white-space:nowrap}
.shot{top:716px;width:148px;height:102px}
.pager{left:334px;top:834px;width:73px;height:19px;background:var(--red-dark);display:flex;justify-content:space-between;align-items:center;padding:0 12px}
.about-title{left:0;top:890px;width:741px;text-align:center;font:400 14px "Raleway",sans-serif;color:#444;letter-spacing:.3px}
.about-text{left:115px;top:917px;width:511px;text-align:center;font-size:6px;line-height:13.3px;color:var(--muted)}
.cta{left:306px;top:971px;width:128px;height:27px;background:var(--red);border:1px solid #8d0c11;color:var(--white);font:400 8px "Open Sans",sans-serif;display:flex;align-items:center;justify-content:center}
.footer{left:0;top:1028px;width:741px;height:140px;background:var(--footer)}
.footer-title{top:1040px;font:700 8px "Open Sans",sans-serif;color:var(--white);letter-spacing:.2px}
.tweet{left:81px;width:190px;font-size:6px;line-height:11px;color:#bbb}
.tweet .bird{left:0;top:2px;width:16px;height:16px;border-radius:50%;background:var(--white)}
.tweet p{margin-left:23px}
.tweet em{font-style:normal;color:var(--red)}
.contact{left:303px;top:1062px;width:170px;font-size:6px;line-height:12.5px;color:#bbb}
.contact .row{display:flex;gap:7px;align-items:flex-start}
.contact .row i{width:5px;height:5px;margin-top:4px;background:var(--red);border-radius:50%;flex:none}
.field{left:502px;width:150px;height:22px;border:1px solid #555b63;font-size:6px;color:#aaa;padding:8px 9px}
.subscribe{left:502px;top:1125px;width:65px;height:22px;background:var(--red);border:1px solid #e33;color:var(--white);font-size:7.5px;display:flex;align-items:center;justify-content:center}
.bottom{left:0;top:1168px;width:741px;height:32px;background:var(--footer-deep)}
.copyright{left:65px;top:1181px;font-size:6px;color:#ccc}
.social{left:572px;top:1175px;display:flex;gap:6px}
.social i{width:18px;height:18px;border:1px solid #888;border-radius:50%}
</style>
</head>
<body>
<div class="abs top-rule"></div>
<div class="abs brand"><span class="mark"></span>RIDGELINE BUILDERS, INC.</div>
<nav class="abs nav"><span class="active">HOME</span><span>PROJECTS</span><span>WHAT WE DO</span><span>ABOUT US</span><span>BLOG</span><span>CONTACT US</span></nav>

<div class="abs hero" role="img" aria-label="Businessman in suit holding a hard hat, sketching a city skyline on a wall"></div>
<div class="abs hero-caption">
  <div class="arrow"><svg width="8" height="8" viewBox="0 0 8 8"><path d="M5.5 1 2.5 4l3 3" stroke="#333" stroke-width="1.5" fill="none"/></svg></div>
  <h1>We are a General Engineering contracting firm</h1>
  <div class="arrow"><svg width="8" height="8" viewBox="0 0 8 8"><path d="M2.5 1 5.5 4l-3 3" stroke="#333" stroke-width="1.5" fill="none"/></svg></div>
</div>

<section class="abs service" style="left:61px;top:424px">
  <div class="abs thumb" style="background:linear-gradient(135deg,#3a7fb5,#9cc3d8)" role="img" aria-label="Business handshake"></div>
  <h2 class="abs">Commercial</h2>
  <p class="abs">It is a long established fact that a reader will be distracted by the readable content of a page when looking at its layout. The point of using Lorem is that it has a more-or-less normal distribution of letters, as opposed uncover many web sites still in their infancy...</p>
  <span class="abs more">Read More &nbsp;»</span>
</section>
<section class="abs service" style="left:382px;top:424px">
  <div class="abs thumb" style="background:linear-gradient(135deg,#6b2a1c,#c7793e)" role="img" aria-label="Restaurant dining room interior"></div>
  <h2 class="abs">Restaurants</h2>
  <p class="abs">It is a long established fact that a reader will be distracted by the readable content of a page when looking at its layout. The point of using Lorem is that it has a more-or-less normal distribution of letters, as opposed uncover many web sites still in their infancy...</p>
  <span class="abs more">Read More &nbsp;»</span>
</section>
<section class="abs service" style="left:61px;top:535px">
  <div class="abs thumb" style="background:linear-gradient(135deg,#b9cfe0,#a27aa8)" role="img" aria-label="Woman in a bright renovated office"></div>
  <h2 class="abs">Tenant Improvement</h2>
  <p class="abs">It is a long established fact that a reader will be distracted by the readable content of a page when looking at its layout. The point of using Lorem is that it has a more-or-less normal distribution of letters, as opposed uncover many web sites still in their infancy...</p>
  <span class="abs more">Read More &nbsp;»</span>
</section>
<section class="abs service" style="left:382px;top:535px">
  <div class="abs thumb" style="background:linear-gradient(135deg,#3f6b2e,#a6b98d)" role="img" aria-label="Worker flushing a fire hydrant on a street"></div>
  <h2 class="abs">Public Works</h2>
  <p class="abs">It is a long established fact that a reader will be distracted by the readable content of a page when looking at its layout. The point of using Lorem is that it has a more-or-less normal distribution of letters, as opposed uncover many web sites still in their infancy...</p>
  <span class="abs more">Read More &nbsp;»</span>
</section>

<div class="abs band"></div>
<div class="abs tabs">
  <svg width="619" height="31" viewBox="0 0 619 31">
    <polygon points="0,0 77,0 67,31 0,31" fill="#9c0d13"/>
    <polygon points="77,0 161,0 151,31 67,31" fill="#b8141a"/>
    <g stroke="rgba(255,255,255,.3)" stroke-width="1">
      <line x1="161" y1="0" x2="151" y2="31"/>
      <line x1="247" y1="0" x2="237" y2="31"/>
      <line x1="341" y1="0" x2="331" y2="31"/>
      <line x1="413" y1="0" x2="403" y2="31"/>
      <line x1="493" y1="0" x2="483" y2="31"/>
      <line x1="553" y1="0" x2="543" y2="31"/>
    </g>
  </svg>
  <span class="abs tab-label" style="left:89px">ALL PROJECTS</span>
  <span class="abs tab-label" style="left:173px">BUILDINGS</span>
  <span class="abs tab-label" style="left:249px">INTERIOR DESIGN</span>
  <span class="abs tab-label" style="left:346px">ISOLATION</span>
  <span class="abs tab-label" style="left:422px">PLUMBING</span>
  <span class="abs tab-label" style="left:497px">TILING</span>
</div>
<div class="abs shot" style="left:61px;background:linear-gradient(135deg,#c9a63c,#5a4e3c)" role="img" aria-label="Engineer with blueprints beside an excavator"></div>
<div class="abs shot" style="left:218px;background:linear-gradient(135deg,#4d86c4,#9aa3aa)" role="img" aria-label="Worker holding a yellow hard hat near a building frame"></div>
<div class="abs shot" style="left:375px;background:linear-gradient(135deg,#6fa8d8,#3b4a5c)" role="img" aria-label="Engineer in a suit in front of towers and cranes"></div>
<div class="abs shot" style="left:532px;background:linear-gradient(135deg,#dfe3e6,#9a8f80)" role="img" aria-label="Architectural model of skyscrapers on blueprints"></div>
<div class="abs pager">
  <svg width="8" height="10" viewBox="0 0 8 10"><path d="M6 1 2 5l4 4" stroke="#fff" stroke-width="1.5" fill="none"/></svg>
  <svg width="10" height="19" viewBox="0 0 10 19"><path d="M9 0 1 19" stroke="rgba(255,255,255,.35)"/></svg>
  <svg width="8" height="10" viewBox="0 0 8 10"><path d="M2 1l4 4-4 4" stroke="#fff" stroke-width="1.5" fill="none"/></svg>
</div>

<h2 class="abs about-title">ABOUT OUR COMPANY</h2>
<p class="abs about-text">It is a long established fact that a reader will be distracted by the readable content of a page when looking at its layout. The point of using Lorem Ipsum is that it has a more-or-less normal distribution of letters, as opposed to using 'Content here, content here', making it look like readable English. Many desktop publishing packages and web page editors now use Lorem Ipsum as their default model text, and a search for 'lorem ipsum' will uncover many web sites still in their infancy.</p>
<div class="abs cta">CLICK HERE FOR MORE INFO</div>

<footer class="abs footer"></footer>
<h3 class="abs footer-title" style="left:81px">LATEST TWEET</h3>
<h3 class="abs footer-title" style="left:303px">CONTACT US</h3>
<h3 class="abs footer-title" style="left:502px">NEWSLETTER</h3>
<div class="abs tweet" style="top:1064px"><span class="abs bird"></span><p>Further convenience is <em>added to the portable</em> air condi temperature until you're fully comfortable.<br>Jun. 29, 2014</p></div>
<div class="abs tweet" style="top:1109px"><span class="abs bird"></span><p>Further convenience is <em>added to the portable</em> air condi temperature until you're fully comfortable.<br>Jun. 29, 2014</p></div>
<div class="abs contact">
  <p>Beat the heat in any room of your house with our wide selection of portable air conditioners.</p>
  <div class="row" style="margin-top:7px"><i></i><span>256 Lorem Ipsum Dummy<br>Lorem</span></div>
  <div class="row"><i></i><span>(000)-555-0142</span></div>
  <div class="row"><i></i><span>info@ridgelinebuilders.com</span></div>
</div>
<div class="abs field" style="top:1063px">Enter Your Name :</div>
<div class="abs field" style="top:1094px">Enter Your Password :</div>
<div class="abs subscribe">SUBSCRIBE</div>

<div class="abs bottom"></div>
<p class="abs copyright">© Copy Rights 2014 Ridgeline Builders Inc.All Rights Reserved</p>
<div class="abs social"><i></i><i></i><i></i><i></i><i></i></div>
</body>
</html>
```